High-End Medical Center Website Design Project

This design is part of a well thought-out project by an experienced project manager / developer. The approved wireframe is attached. Creative interpretations / suggestions based on the layout encouraged.

The design is for a new state-of-the-art medical center located in Dallas, Texas. The target audience would likely be individuals (approx. 60% female /40% male) who are the healthcare decision-makers for their families. They would likely have insurance and be inclined to seek out top-quality care.

Potential clients would choose this client over others in their industry because the medical center is physician owned, meaning it is patient-focused rather than profit-focused. The facility is brand new, featuring the latest technology. (This includes an amazing waiting room featuring WiFi and docking stations.) The physicians are hand-picked by referral only.

The look of the site should be extremely clean. We are going for a well-organized, professional look with a bit of a warm glow (interpret that however you like). Use crisp corners and the colors in the logo.

Think modern, clean with some great use of color / font.

We can get lovely photography of the medical center once construction is complete. Feel free to use an "example image" behind the Featured Area ("Physician Owned. Patient-Focused") if you like. We are open to ideas.

ONE CHANGE REQUESTED IN THE WIREFRAME:

Remove the "Connect" 1/4 page footer area and replace with a quick contact form. You may swap the "Locations" area with the form if desired. Put social media icons at the top left of the page in the top header area.

(Note: Please use social media icons that match the design rather than standard icons. We preferred not placing the icons at the top, but the client requested this. Let's not bring more attention to them than necessary.)
Updates

We're custom programming this site, so there's no need to base it on a template. Also, we would prefer not to use typical "seen everywhere" stock images.Thanks.

Industry/Entity Type

Construction

Requirements
Must have
• Follow the wireframe. This has been approved.
Nice to have
• Examples of what hover states, links or dropdowns might look like.

```html
<!DOCTYPE html>
<html lang="fr">
<head>
<meta charset="utf-8">
<title>Nova Medical Center</title>
<link href="https://fonts.googleapis.com/css2?family=Open+Sans:ital,wght@0,400;0,600;0,700;1,400&display=swap" rel="stylesheet">
<style>
:root{
  --blue:#1a5fa8;
  --blue-dark:#0f4a86;
  --teal:#3fa6b4;
  --teal-dark:#2b8796;
  --ink:#333;
  --muted:#555;
  --line:#e3e3e3;
  --hero-a:#2d4f7a;
  --hero-b:#1a3256;
  --foot:#3b3b3b;
  --foot-bottom:#2f2f2f;
  --foot-text:#c8c8c8;
}
*{margin:0;padding:0;box-sizing:border-box}
html,body{width:983px;height:1200px;overflow:hidden;background:#fff}
body{font-family:"Open Sans",Arial,sans-serif;color:var(--ink)}
.page{width:1200px;height:1465px;position:relative;transform:scale(.81917);transform-origin:0 0}
.abs{position:absolute}

/* top bar */
.topbar{left:0;top:0;width:1200px;height:28px;border-bottom:1px solid #eee}
.social{left:808px;top:7px;display:flex;gap:10px}
.social span{width:14px;height:14px;border-radius:50%;background:#b5b5b5;display:block}
.phone{left:948px;top:2px;font-size:16px;font-weight:600;color:#8c8c8c;display:flex;align-items:center;gap:8px}
.topbar .sep{left:922px;top:4px;width:1px;height:18px;background:#ddd}

/* header */
.header{left:0;top:28px;width:1200px;height:95px;background:linear-gradient(#fff,#f6f6f6);border-bottom:1px solid #cfcfcf}
.brand{left:100px;top:29px;display:flex;align-items:center;gap:10px;font-size:26px;font-weight:700;color:var(--blue);letter-spacing:1px}
.brand i{width:30px;height:30px;background:var(--blue);display:block}
.nav{right:100px;top:30px;display:flex;gap:0;font-size:14px}
.nav a{color:var(--ink);text-decoration:none;padding:6px 12.5px 8px;display:block}
.nav a.active{background:var(--teal);color:#fff;border-bottom:3px solid var(--teal-dark);padding:6px 6px 5px;margin-right:8px}
.nav a:last-child{padding-right:0}

/* hero */
.hero{left:0;top:123px;width:1200px;height:449px;background:linear-gradient(160deg,var(--hero-a),var(--hero-b));overflow:hidden}
.hero h1{position:absolute;left:0;top:52px;width:1200px;text-align:center;color:#fff;font-size:41px;font-weight:700}
.hero svg{position:absolute;left:0;top:0}

/* tabs */
.tabline{left:100px;top:581px;width:1000px;height:3px;background:#e6e6e6}
.tabline b{position:absolute;left:335px;top:0;width:331px;height:3px;background:var(--blue)}

/* features */
.ribbon{left:100px;top:666px}
.ribbon span{position:absolute;left:26px;top:20px;color:#fff;font-size:20px;font-weight:700;white-space:nowrap}
.feature{top:630px;width:220px;text-align:center}
.feature h3{display:flex;align-items:center;justify-content:center;gap:8px;font-size:18px;font-weight:400;color:var(--teal-dark);margin-bottom:14px}
.feature h3 i{width:34px;height:34px;border-radius:50%;background:var(--teal);display:flex;align-items:center;justify-content:center}
.feature p{font-size:11px;line-height:17px;color:#444}
.btn{display:inline-block;background:linear-gradient(#2a74bd,var(--blue-dark));color:#fff;font-size:13px;border-radius:12px;padding:2px 14px 3px;box-shadow:0 2px 0 #9fb7cc;text-decoration:none}
.feature .btn{margin-top:18px}

/* welcome */
.section-title{font-size:22px;color:var(--blue);font-weight:400}
.rule{height:1px;background:var(--line)}
.rule b{position:absolute;left:0;top:-1px;width:50px;height:3px;background:var(--teal)}
.photo{left:100px;top:904px;width:177px;height:158px;background:linear-gradient(#c9d2e6,#eee6df 55%,#b89c84);border:1px solid #ccc}
.welcome-text{left:298px;top:900px;width:445px;font-size:13px;line-height:20px;color:#444}
.welcome-text p{margin-bottom:6px}

/* testimonials */
.quote{left:782px;top:879px;width:318px;height:160px;border:1px solid var(--line);border-top:none}
.quote p{position:absolute;left:30px;top:16px;width:280px;font-size:12px;line-height:20px;font-style:italic;color:#444}
.quote p+p{top:82px}
.quote .mark{position:absolute;left:6px;top:8px;font-size:28px;color:#999;font-style:italic;font-family:Georgia,serif}
.author{left:850px;top:1043px;font-size:14px;color:var(--teal)}
.arrows{left:1061px;top:1048px;display:flex;gap:5px}
.arrows span{width:16px;height:16px;border-radius:50%;background:#444;color:#fff;font-size:10px;line-height:15px;text-align:center}

/* footer */
.footer{left:0;top:1118px;width:1200px;height:302px;background:var(--foot)}
.fcol{top:48px;color:var(--foot-text);font-size:11px;line-height:17px}
.fcol h4{color:#fff;font-size:16px;font-weight:600;margin-bottom:14px}
.item{display:flex;gap:9px;margin-bottom:16px;width:180px}
.thumb{width:50px;height:48px;flex:none;background:linear-gradient(#e8eef3,#9fb6c9)}
.form label{display:block;margin-bottom:4px}
.form .field{width:172px;height:20px;background:#f1f1f1;border:1px solid #ddd;margin-bottom:8px}
.form .area{height:40px}
.form .btn{font-size:10px;padding:0 11px;margin-top:4px;background:linear-gradient(#52b4c2,var(--teal-dark));box-shadow:0 1px 0 #222}
.fcol .para{margin-bottom:14px}
.wait{display:flex;align-items:baseline;gap:6px;color:#fff;margin:-6px 0 10px}
.wait strong{font-size:48px;font-weight:700;line-height:56px}
.wait span{font-size:26px}
.copy{left:0;top:1420px;width:1200px;height:45px;background:var(--foot-bottom);color:#fff;font-size:11px}
.copy .l{left:100px;top:14px}
.copy .r{right:100px;top:14px}
</style>
</head>
<body>
<div class="page">

  <div class="abs topbar">
    <div class="abs social"><span></span><span></span><span></span><span></span></div>
    <div class="abs sep"></div>
    <div class="abs phone">
      <svg width="20" height="18" viewBox="0 0 20 18"><path d="M2 2h16v10H8l-4 4v-4H2z" fill="#bbb"/></svg>
      (555) 014-2290
    </div>
  </div>

  <div class="abs header">
    <div class="abs brand"><i></i>NOVA MEDICAL CENTER</div>
    <nav class="abs nav">
      <a class="active" href="#">Why Nova</a><a href="#">Physicians</a><a href="#">Specialties</a><a href="#">Info</a><a href="#">Locations</a><a href="#">Contact</a>
    </nav>
  </div>

  <section class="abs hero" role="img" aria-label="Blurred exterior photo of the medical center building">
    <h1>Physician Owned. Patient Focused</h1>
    <svg width="1200" height="449">
      <g stroke="#7f95b0" stroke-width="1" fill="none" opacity=".8">
        <line x1="128" y1="159" x2="586" y2="159"/><line x1="160" y1="177" x2="586" y2="177"/>
        <line x1="614" y1="159" x2="1072" y2="159"/><line x1="614" y1="177" x2="1040" y2="177"/>
        <line x1="130" y1="389" x2="1070" y2="389" opacity=".5"/>
        <line x1="320" y1="355" x2="320" y2="389" opacity=".5"/><line x1="600" y1="355" x2="600" y2="389" opacity=".5"/><line x1="880" y1="355" x2="880" y2="389" opacity=".5"/>
      </g>
      <g fill="#c6d0dc"><circle cx="586" cy="159" r="3.5"/><circle cx="586" cy="177" r="3.5"/><circle cx="614" cy="159" r="3.5"/><circle cx="614" cy="177" r="3.5"/></g>
      <g fill="#45a9b7" stroke="#3592a0" stroke-width="2">
        <circle cx="320" cy="297" r="57"/><circle cx="600" cy="297" r="57"/><circle cx="880" cy="297" r="57"/>
      </g>
      <!-- stethoscope -->
      <g fill="none" stroke="#fff" stroke-width="5" stroke-linecap="round">
        <path d="M313 263v18c0 14 26 14 26 0v-18"/>
        <path d="M326 295v12c0 16-16 22-24 10"/>
        <circle cx="298" cy="312" r="6"/>
      </g>
      <!-- folder plus -->
      <path d="M565 275h22l6 6h44v48h-72z" fill="#fff"/>
      <path d="M601 289v28M587 303h28" stroke="#45a9b7" stroke-width="5"/>
      <!-- question -->
      <text x="880" y="328" text-anchor="middle" font-family="Georgia,serif" font-size="86" font-weight="700" fill="#fff">?</text>
    </svg>
  </section>

  <div class="abs tabline"><b></b></div>

  <div class="abs ribbon">
    <svg width="245" height="80"><path d="M3 3h215l22 34-22 34H3l6-34z" fill="#1466b8"/><path d="M3 71h215l22-34 4 4-22 37H8z" fill="#9fb4c8" opacity=".6"/></svg>
    <span>What Sets us Apart</span>
  </div>

  <div class="abs feature" style="left:366px">
    <h3><i><svg width="20" height="20" viewBox="0 0 20 20"><circle cx="10" cy="10" r="8" fill="none" stroke="#fff" stroke-width="2"/><path d="M2 10h16M10 2c-4 5-4 11 0 16M10 2c4 5 4 11 0 16" stroke="#fff" fill="none" stroke-width="1.5"/></svg></i>TECHNOLOGY</h3>
    <p>Le Lorem Ipsum est simplement du faux texte employé dans la compos ition et la mise en page avanti mpressione Lorem.</p>
    <a class="btn" href="#">More</a>
  </div>
  <div class="abs feature" style="left:616px">
    <h3><i><svg width="20" height="20"><path d="M4 10l5 5 8-10" stroke="#fff" stroke-width="3" fill="none"/></svg></i>QUALITY OF CORE</h3>
    <p>Le Lorem Ipsum est simplement du faux texte employé dans la compos ition et la mise en page avanti mpressione Lorem.</p>
    <a class="btn" href="#">More</a>
  </div>
  <div class="abs feature" style="left:866px">
    <h3><i><svg width="20" height="20"><circle cx="9" cy="7" r="4" fill="#fff"/><path d="M2 18c0-6 14-6 14 0z" fill="#fff"/><circle cx="15" cy="15" r="4" fill="#fff" stroke="#3fa6b4"/></svg></i>PATIENT EXPERIENCE</h3>
    <p>Le Lorem Ipsum est simplement du faux texte employé dans la compos ition et la mise en page avanti mpressione Lorem.</p>
    <a class="btn" href="#">More</a>
  </div>

  <h2 class="abs section-title" style="left:100px;top:841px">Welocme to Nova Medical Center</h2>
  <div class="abs rule" style="left:100px;top:879px;width:640px"><b></b></div>
  <div class="abs photo" role="img" aria-label="Photo of the bright hospital lobby with artwork on the walls"></div>
  <div class="abs welcome-text">
    <p>Plusieurs variations de Lorem Ipsum peuvent être trouvées ici ou là, mais la majeure partie d'entre elles a été altérée par l'addition d'humour ou de mots aléatoires qui.</p>
    <p>Ne ressemblent pas une seconde à du texte standard. Si vous voulez utiliser un passage du Lorem Ipsum, vous devez être sûr qu'il n'y a rien d'embarrassant caché dans le texte.</p>
    <a class="btn" href="#" style="margin-top:4px">More</a>
  </div>

  <h2 class="abs section-title" style="left:782px;top:841px">Testimonials</h2>
  <div class="abs rule" style="left:782px;top:879px;width:318px"><b></b></div>
  <div class="abs quote">
    <span class="mark">“</span>
    <p>On sait depuis longtemps que travailler avec du texte lisible et contenant du sens est source de distractions.</p>
    <p>Et empêche de se concentrer sur la mise en page elle-même. L'avantage du Lorem Ipsum sur un texte générique comme 'Du texte. Du texte.</p>
  </div>
  <svg class="abs" style="left:800px;top:1037px" width="42" height="22"><path d="M0 1l38 20V1" fill="#fff" stroke="#e3e3e3"/><path d="M2 0h35" stroke="#fff" stroke-width="2"/></svg>
  <div class="abs author">Marcus Hale</div>
  <div class="abs arrows"><span>←</span><span>→</span></div>

  <footer class="abs footer">
    <div class="abs fcol" style="left:100px">
      <h4>News</h4>
      <div class="item"><div class="thumb" role="img" aria-label="Doctor portrait"></div><div>Contrairement à une opinion répandue, le Lorem Ipsum.</div></div>
      <div class="item"><div class="thumb" role="img" aria-label="Medical staff photo"></div><div>Contrairement à une opinion répandue, le Lorem Ipsum.</div></div>
      <div class="item"><div class="thumb" role="img" aria-label="Patient photo"></div><div>Contrairement à une opinion répandue, le Lorem Ipsum.</div></div>
    </div>
    <div class="abs fcol" style="left:310px">
      <h4>Blog</h4>
      <div class="item"><div class="thumb" role="img" aria-label="Doctor on phone"></div><div>Contrairement à une opinion répandue, le Lorem Ipsum.</div></div>
      <div class="item"><div class="thumb" role="img" aria-label="Surgeon photo"></div><div>Contrairement à une opinion répandue, le Lorem Ipsum.</div></div>
      <div class="item"><div class="thumb" role="img" aria-label="Physician photo"></div><div>Contrairement à une opinion répandue, le Lorem Ipsum.</div></div>
    </div>
    <div class="abs fcol form" style="left:510px">
      <h4>Contact Form</h4>
      <label>Name:</label><div class="field"></div>
      <label>Email Address:</label><div class="field"></div>
      <label>Comments:</label><div class="field area"></div>
      <a class="btn" href="#">More</a>
    </div>
    <div class="abs fcol" style="left:711px;width:175px">
      <h4>Location</h4>
      <p class="para">Contrairement à une opinionrépa \ndue, le Lorem Ipsum.n'est passimplement.</p>
      <p class="para">Très populaire pendant la Renais-sance, est un traité sur la théorie de l'éthique.</p>
      <p class="para">Le Lorem Ipsum ainsi obtenu ne contient aucune répétition, ni ne contient des.</p>
    </div>
    <div class="abs fcol" style="left:909px;width:180px">
      <h4>Average wait Time</h4>
      <div class="wait"><strong>9</strong><span>Minutes</span></div>
      <p>Très populaire pendant la Renais-sance, est un traité sur la théorie de l'éthique. Les premières lignes du Lorem Ipsum, "Lorem ipsum dolor sit ametLe Lorem Ipsum ainsi obtenu ne contient aucune répétition.</p>
    </div>
  </footer>

  <div class="abs copy">
    <span class="abs l">© Copyrights 2013 All rights Reserved</span>
    <span class="abs r">Sitemap &nbsp;|&nbsp; Privacy</span>
  </div>

</div>
</body>
</html>
```